Ad For Home Magazine for Landscape Architecture company

Hi Designers,

We are a dedicated landscape architecture and outdoor construction company. We need a little help with an ad design for a magazine.

Our approach should be elegant but accessible. Our clientele is high end.

visit our site to get to know us and get our style: www.verdanhome.com

The focus of this ad will be in Outdoor living spaces | custom outdoor kitchens and premium outdoor kitchen appliances. as such the images chosen should showcase all of these.

Ad Specs: Full Page, see attachment.

Images: 1-4 images total for the ad. choose from pictures upload

Logo: Orginal Logo and logo variation included.

Showroom section: (optional) images for the showroom are included. this section is optional and up to the designer.

Text 1: Outdoor Living Spaces| Custom Outdoor Kitchens | Premium Appliances
Text 2 ( Company info) 212.638.9024 | Verdanhome.com | 4172 SE 52 ST, Doral FL 33178

Target Market(s)

High end

Industry/Entity Type

Architecture

Font styles to use
Serif
Sans Serif

Colors

Designer to choose colors to be used in the design.

Requirements
Must have
• Text:
• - Custom Outdoor Living Spaces | Outdoor Kitchens | Appliances
• - Company Info
• - Logo
• - Pictures (1-4)
Nice to have
• A showroom section or picture - only if the design works
Should not have
• Any

```html
<!DOCTYPE html>
<html lang="en">
<head>
<meta charset="utf-8">
<title>Outdoor Living Spaces – Verdanhome</title>
<link rel="stylesheet" href="https://fonts.googleapis.com/css2?family=Cinzel:wght@400;500&family=Lato:wght@300;400&display=swap">
<style>
  :root {
    --backdrop: #dcdcdc;
    --paper: #f1f1f0;
    --ink: #1c1c1c;
    --forest: #43694b;
    --leaf: #8fc65a;
    --brand: #2f7d3a;
    --rule: #444;
  }
  * { margin: 0; padding: 0; box-sizing: border-box; }
  html, body {
    width: 1200px; height: 1200px; overflow: hidden;
    background: var(--backdrop);
  }
  .ad-page {
    position: absolute; left: 207px; top: 20px;
    width: 786px; height: 1160px;
    background: var(--paper);
    box-shadow: 0 6px 24px rgba(0,0,0,.18);
  }
  .photo { position: absolute; }
  .photo--pergola {
    left: 0; top: 0; width: 390px; height: 322px;
    background: linear-gradient(180deg, #3a3d42 0%, #6f8a8f 35%, #8ea3a8 60%, #b9c2c7 100%);
  }
  .photo--pool {
    left: 394px; top: 0; width: 392px; height: 322px;
    background: linear-gradient(180deg, #b9d2e6 0%, #6b7a64 40%, #d9d5cc 62%, #2a8fc4 100%);
  }
  .photo--kitchen {
    left: 0; top: 661px; width: 390px; height: 325px;
    background: linear-gradient(180deg, #3c3c3c 0%, #7aa1a5 35%, #9a9a9a 60%, #3a3d40 100%);
  }
  .photo--showroom {
    left: 394px; top: 661px; width: 392px; height: 325px;
    background: linear-gradient(180deg, #2d2f33 0%, #cfd6d8 38%, #a5b6c4 60%, #6d4c36 100%);
  }
  .side-bar {
    position: absolute; top: 358px; width: 36px; height: 267px;
    background: var(--forest);
  }
  .side-bar--left { left: 0; }
  .side-bar--right { right: 0; }
  .title-frame {
    position: absolute; left: 63px; top: 358px; width: 650px; height: 267px;
    border: 1px solid var(--rule);
    padding: 3px;
    background: var(--paper);
  }
  .title-frame__inner {
    width: 100%; height: 100%;
    border: 8px solid var(--leaf);
    outline: 1px solid var(--rule);
    outline-offset: -9px;
    display: flex; flex-direction: column; align-items: center; justify-content: center;
    color: var(--ink);
    font-family: "Cinzel", serif;
  }
  .headline {
    font-size: 72px; font-weight: 400; letter-spacing: 8px; line-height: 1;
    margin-left: 20px;
  }
  .headline-sub {
    font-size: 46px; font-weight: 400; letter-spacing: 6px; line-height: 1;
    margin-top: 4px; margin-left: 20px;
  }
  .headline-rule {
    width: 572px; height: 1px; background: var(--rule); margin-top: 10px;
  }
  .tagline {
    font-size: 19px; letter-spacing: 1.5px; margin-top: 10px;
  }
  .brand {
    position: absolute; left: 0; right: 0; top: 1040px;
    display: flex; align-items: center; justify-content: center; gap: 10px;
  }
  .brand__mark { width: 34px; height: 34px; background: var(--brand); }
  .brand__name {
    font-family: "Cinzel", serif; font-size: 32px; font-weight: 500;
    color: var(--brand); letter-spacing: 1px;
  }
  .contact {
    position: absolute; left: 0; right: 0; top: 1088px;
    text-align: center;
    font-family: "Lato", sans-serif; font-weight: 300; font-size: 17px;
    color: var(--ink); letter-spacing: .3px;
  }
</style>
</head>
<body>
  <main class="ad-page">
    <div class="photo photo--pergola" role="img" aria-label="Covered pergola patio with bar seating and lounge sofas"></div>
    <div class="photo photo--pool" role="img" aria-label="Outdoor kitchen bar beside a swimming pool and lake"></div>

    <div class="side-bar side-bar--left"></div>
    <div class="side-bar side-bar--right"></div>
    <section class="title-frame">
      <div class="title-frame__inner">
        <h1 class="headline">OUTDOOR</h1>
        <h2 class="headline-sub">LIVING SPACES</h2>
        <div class="headline-rule"></div>
        <p class="tagline">Custom Outdoor Kitchens &amp; Premium Appliances</p>
      </div>
    </section>

    <div class="photo photo--kitchen" role="img" aria-label="Stainless grill and granite countertop outdoor kitchen with wine glasses"></div>
    <div class="photo photo--showroom" role="img" aria-label="Showroom with outdoor lounge furniture under a shade sail"></div>

    <div class="brand">
      <span class="brand__mark"></span>
      <span class="brand__name">VERDANHOME</span>
    </div>
    <p class="contact">212.638.9024 | 4172 SE 52 ST, DORAL FL 33178 | WWW.VERDANHOME.COM</p>
  </main>
</body>
</html>
```